Website Redesign

I am looking to have our website redone. We recently paid to have this done and are very unhappy with the results. We're looking to have a much more modern and clean feeling while GREATLY enhancing the user experience. We are very close to have a new logo designed as well as having some brand colors (Pantone 3005C). We want our site to have a human feel to it without focusing completely on our products. That being said, we need our products to play a more prominent role as our current site doesn't very clearly display what we do.
Our website: kvhomewares.com
Websites we like (overall feel): jogluma.com, oswaldtrent.com
Websites we like (functionality): birchvault.com
Updates
I apologize, we are new to ArtHivePro. I am showing a budget of $500 for this project. I know we'd go beyond that. I do not believe that we'll be able to overhaul our website for $500. I apologize for any confusion.

```html
<!DOCTYPE html>
<html lang="en">
<head>
<meta charset="utf-8">
<title>KV Homewares</title>
<link href="https://fonts.googleapis.com/css2?family=Fira+Sans+Condensed:wght@500;600&family=Source+Sans+3:wght@300;400;600&display=swap" rel="stylesheet">
<style>
:root{
  --blue:#1e4fa6;
  --blue-dark:#0d3484;
  --nav-top:#5390de;
  --nav-bottom:#2c63c2;
  --heading:#1d4da2;
  --text:#6a6a6a;
  --grey-line:#d8d8d8;
  --footer-bg:#f2f2f2;
  --white:#ffffff;
}
*{box-sizing:border-box;margin:0;padding:0}
html,body{width:1200px;height:1115px;overflow:hidden;background:var(--white);font-family:"Source Sans 3",sans-serif}
.page{position:relative;width:1200px;height:1115px}
.account-links{position:absolute;left:80px;top:14px;font-size:14px;color:#666}
.account-links span{margin:0 6px;color:#999}
.search{position:absolute;left:896px;top:26px;width:237px;height:30px;border:1px solid #bbb;border-radius:15px;background:linear-gradient(#fafafa,#ececec);font-size:13px;font-style:italic;color:#9a9a9a;padding:6px 16px}
.search svg{position:absolute;right:8px;top:5px}
.nav{position:absolute;left:0;top:77px;width:1200px;height:54px;background:linear-gradient(var(--nav-top),var(--nav-bottom));border-bottom:1px solid #1f4f9f}
.nav a{position:absolute;top:0;height:54px;line-height:54px;color:var(--white);text-decoration:none;font-family:"Fira Sans Condensed",sans-serif;font-weight:500;font-size:19px}
.nav .sep{position:absolute;top:0;width:1px;height:54px;background:rgba(255,255,255,.35)}
.brand{position:absolute;left:518px;top:11px;width:162px;height:162px;border-radius:50%;background:var(--white);box-shadow:0 1px 4px rgba(0,0,0,.2);display:flex;align-items:center;justify-content:center}
.brand-mark{width:140px;height:140px;border-radius:50%;background:var(--blue);display:flex;align-items:center;justify-content:center;color:var(--white);font-size:19px;font-weight:400;text-align:center;line-height:1.1}
.hero{position:absolute;left:0;top:131px;width:1200px;height:529px;background:radial-gradient(ellipse at 25% 45%,#c79b82 0%,#8f6e5d 30%,#5a4a41 60%,#3a322d 100%)}
.hero-copy{position:absolute;left:618px;top:175px;color:var(--white)}
.hero-kicker{font-family:"Fira Sans Condensed",sans-serif;font-weight:600;font-size:36px;line-height:38px}
.hero-title{font-family:"Fira Sans Condensed",sans-serif;font-weight:600;font-size:51px;line-height:52px}
.hero-text{font-size:18px;font-weight:300;line-height:26px;margin-top:12px;width:470px}
.btn{display:inline-block;border-radius:20px;background:linear-gradient(#3f78cf,#0f3e92);color:var(--white);text-align:center;box-shadow:0 1px 2px rgba(0,0,0,.4)}
.hero .btn{position:absolute;left:621px;top:334px;width:123px;height:38px;line-height:38px;font-size:14px;font-weight:600}
.arrow{position:absolute;top:204px}
.welcome{position:absolute;left:67px;top:695px;width:581px;height:251px;border:1px solid var(--grey-line);border-radius:20px}
.welcome h1{position:absolute;left:33px;top:18px;font-size:27px;font-weight:400;color:var(--heading)}
.welcome p{position:absolute;left:35px;top:62px;width:300px;font-size:14px;font-weight:300;line-height:23px;color:var(--text)}
.welcome .btn{position:absolute;left:35px;top:189px;width:102px;height:33px;line-height:33px;font-size:11px;font-weight:600}
.product-shot{position:absolute;left:365px;top:50px;width:167px;height:166px;border-radius:8px;background:radial-gradient(circle,#c9a889 0%,#b89877 40%,#ffffff 72%)}
.dots{position:absolute;left:550px;top:97px}
.dots i{display:block;width:12px;height:12px;border-radius:50%;background:#c0d3ef;margin-bottom:4px}
.dots i.on{background:var(--blue)}
.products{position:absolute;left:670px;top:695px;width:461px;height:247px;border-radius:20px;background:linear-gradient(#3e76d0,#0e3487);color:var(--white)}
.products h2{position:absolute;left:34px;top:16px;font-size:27px;font-weight:400}
.products p{position:absolute;left:35px;top:54px;width:380px;font-size:14px;font-weight:300;line-height:21px;color:#dbe6f7}
.products ul{position:absolute;top:110px;list-style:none;font-size:13.5px;font-weight:400}
.products li{height:25px;padding-left:12px;position:relative}
.products li::before{content:"";position:absolute;left:0;top:5px;border-left:5px solid var(--white);border-top:4px solid transparent;border-bottom:4px solid transparent}
.footer{position:absolute;left:0;top:1004px;width:1200px;height:111px;background:var(--footer-bg);border-top:1px solid #e2e2e2}
.footer-links{position:absolute;left:67px;top:27px;font-size:15.5px;color:var(--blue)}
.footer-links span{margin:0 6px}
.copyright{position:absolute;left:67px;top:58px;font-size:13px;font-weight:300;color:var(--blue)}
.social{position:absolute;left:986px;top:26px;display:flex;gap:5px}
.social i{display:block;width:32px;height:32px;border-radius:50%;background:#a9a9a9}
</style>
</head>
<body>
<div class="page">
  <div class="account-links">Register<span>|</span>My Cart<span>|</span>My Account</div>
  <div class="search">Search here..
    <svg width="20" height="20" viewBox="0 0 20 20"><circle cx="8" cy="8" r="6" fill="none" stroke="#bbb" stroke-width="1.5"/><line x1="12.5" y1="12.5" x2="18" y2="18" stroke="#bbb" stroke-width="2"/></svg>
  </div>

  <nav class="nav">
    <a style="left:147px">HOME</a><span class="sep" style="left:217px"></span>
    <a style="left:240px">PRDOUCTS</a><span class="sep" style="left:350px"></span>
    <a style="left:370px">ORDERING</a>
    <a style="left:733px">WHY</a><span class="sep" style="left:785px"></span>
    <a style="left:805px">COMAPNY</a><span class="sep" style="left:900px"></span>
    <a style="left:918px">CONTACT</a>
  </nav>

  <div class="brand"><div class="brand-mark">KV<br>Homewares</div></div>

  <section class="hero" role="img" aria-label="Portrait photograph of a smiling businesswoman in a warmly lit office">
    <svg class="arrow" style="left:33px" width="32" height="66" viewBox="0 0 32 66"><polyline points="28,4 4,33 28,62" fill="none" stroke="#fff" stroke-width="5"/></svg>
    <svg class="arrow" style="left:1134px" width="32" height="66" viewBox="0 0 32 66"><polyline points="4,4 28,33 4,62" fill="none" stroke="#fff" stroke-width="5"/></svg>
    <div class="hero-copy">
      <div class="hero-kicker">ETIAM EST NUNC VENENATIS</div>
      <div class="hero-title">MAURIS VEL LACUS VITAE</div>
      <div class="hero-text">Mauris vel lacus vitae felis vestibulum volutpat. Etiam est nunc, venenatis in tristique eu imperdiet ac nisl.</div>
    </div>
    <span class="btn">READ MORE</span>
  </section>

  <section class="welcome">
    <h1>Welcome to KV Homewares</h1>
    <p>Mauris vel lacus vitae felis vestibulum volutpat. Etiam est nunc, venenatis in, tristique eu, imperdiet ac, nisl. Cum sociis natoque penatibus et magnis dis parturient montes, nascetur ridiculus mus. In iaculis facilisis massa.</p>
    <span class="btn">VIEW MORE</span>
    <div class="product-shot" role="img" aria-label="Product photo of two round folding tables on castors"></div>
    <div class="dots"><i></i><i></i><i></i><i class="on"></i></div>
  </section>

  <section class="products">
    <h2>Choose Our Products</h2>
    <p>Mauris vel lacus vitae felis vestibulum volutpat Etiam est nunc venenatis in tristique eu imperdiet ac.</p>
    <ul style="left:38px"><li>Chairs</li><li>Double Bed</li><li>Tables</li><li>Seatings</li></ul>
    <ul style="left:172px"><li>Lecturers</li><li>Transport Solutions</li><li>Dinnign Table</li><li>More Products</li></ul>
  </section>

  <footer class="footer">
    <div class="footer-links">Sitemap<span>|</span>Term of Use<span>|</span>Privacy Policy<span>|</span>Contact</div>
    <div class="copyright">© 2013 Company Name.&nbsp; All right reserved</div>
    <div class="social"><i></i><i></i><i></i><i></i></div>
  </footer>
</div>
</body>
</html>
```